Flyer für einen Pflegedienst
Die Kommunikation ist herausragend, es wird sofort in absolut unglaublich schneller Zeit auf Wünsche reagiert. Die Ergebnisse sind perfekt auf die eigenen Wünsche zugeschnitten und passen zum Corporate Design. Die Dateien sind alle samt fehlerfrei, in bester Qualität und können ohne Umwege an die Druckerei gegeben werden. Auch kurzfristige Änderungen nach Fertigstellung wurden sofort durchgeführt. Höflich, respektvoll, zuvorkommend. Mein 1 zu 1 Designer
Zielgruppe
Wir sind ein Pflegedienst, unsere Zielgruppe sind alle Menschen die Unterstützung brauchen. Das sind im Hauptteil Senioren.
Aufgabenstellung
Der Flyer soll im DIN A5 Format designed sein. Der Print soll hochwertig sein. Wir möchten vor allem wohlhabendere Kunden damit ansprechen. Er soll die Kunden direkt packen, aber auch nicht zu viele Informationen beinhalten, die einen überfordern.

```html
<!DOCTYPE html>
<html lang="de">
<head>
<meta charset="utf-8">
<title>Flyer Pflege Lindner</title>
<link href="https://fonts.googleapis.com/css2?family=Nunito:wght@700;800&family=Quicksand:ital,wght@0,400;0,500;0,600;1,500&display=swap" rel="stylesheet">
<style>
:root{
  --navy:#4a5878;
  --heading:#3e4b6e;
  --salmon:#d9736b;
  --paper:#fbfaf5;
  --ink:#333845;
  --frame:#8c8c8c;
  --white:#ffffff;
}
*{margin:0;padding:0;box-sizing:border-box}
html,body{width:1200px;height:852px;overflow:hidden;background:#fff}
body{position:relative;font-family:"Quicksand",sans-serif;color:var(--ink)}
.page{position:absolute;top:15px;width:581px;height:822px;background:var(--paper);border:2px solid var(--frame);overflow:hidden}
.page--front{left:11px}
.page--back{left:608px}
.photo{position:absolute;left:0;top:0;width:100%}
.page--front .photo{height:392px;background:linear-gradient(120deg,#e9d8c8 0%,#c9b6a6 30%,#6f8fbd 55%,#dcdcdc 80%,#9fb3c9 100%)}
.page--back .photo{height:302px;background:linear-gradient(110deg,#6b5444 0%,#b69479 30%,#d9a99e 50%,#5e76b8 70%,#c7a48a 100%)}
.band-dark{position:absolute;left:0;width:100%;background:var(--navy)}
.band-accent{position:absolute;left:100px;right:0;height:13px;background:var(--salmon)}
.page--front .band-dark{top:392px;height:21px}
.page--front .band-accent{top:413px}
.page--back .band-dark{top:302px;height:23px}
.page--back .band-accent{top:325px}
.brand{position:absolute;color:var(--white);display:flex;align-items:center;gap:10px}
.brand-mark{border:3px solid var(--white);border-radius:50%;flex:none}
.brand-name{font-family:"Quicksand",sans-serif;font-weight:600;line-height:1}
.brand-tag{font-size:12px;font-weight:500;margin-top:6px}
.page--front .brand{left:76px;top:290px}
.page--front .brand-mark{width:88px;height:88px}
.page--front .brand-name{font-size:40px}
.page--back .brand{left:290px;top:205px}
.page--back .brand-mark{width:62px;height:62px}
.page--back .brand-name{font-size:28px}
.page--back .brand-tag{font-size:10px;margin-top:4px}
.intro{position:absolute;left:52px;top:456px;width:492px}
h2{font-family:"Nunito",sans-serif;font-weight:800;color:var(--heading);font-size:19px;margin-bottom:6px}
.intro p{font-size:16px;line-height:19.8px;margin-bottom:19.8px}
em{font-style:italic}
.footer{position:absolute;left:0;bottom:0;width:100%;background:var(--navy);color:var(--white)}
.page--front .footer{height:114px}
.contact{position:absolute;top:22px;font-size:14.5px;line-height:23.5px}
.contact--address{left:54px}
.contact--web{left:298px}
.contact li{list-style:none;display:flex;align-items:center;gap:8px}
.contact strong{font-weight:600}
.icon{width:14px;height:14px;flex:none;fill:none;stroke:var(--white);stroke-width:1.4}
.spacer{width:14px;flex:none}
.services{position:absolute;left:50px;top:352px;width:500px}
.services h2{margin-bottom:8px}
.services h3{font-style:italic;font-weight:500;font-size:16px;margin-bottom:3px}
.services ul{margin-bottom:19px;padding-left:24px}
.services li{font-size:16px;line-height:19.7px}
.page--back .footer{height:116px}
.footer-col{position:absolute;top:12px;font-size:13px}
.footer-col h4{font-family:"Nunito",sans-serif;font-weight:700;font-size:13px;margin-bottom:8px}
.footer-col--steps{left:50px}
.footer-col--steps ul{padding-left:24px}
.footer-col li{line-height:16.7px}
.footer-col--care{left:331px;width:205px;line-height:16.7px}
.divider{position:absolute;left:316px;top:12px;width:1px;height:96px;background:var(--white)}
</style>
</head>
<body>

<section class="page page--front">
  <div class="photo" role="img" aria-label="Foto: Pflegerin im blauen Kasack lächelt zwei Seniorinnen zu, eine davon im Rollstuhl mit Teetasse"></div>
  <div class="brand">
    <span class="brand-mark"></span>
    <div>
      <div class="brand-name">Pflege Lindner</div>
      <div class="brand-tag">Miteinander leben, herzlich umsorgen</div>
    </div>
  </div>
  <div class="band-dark"></div>
  <div class="band-accent"></div>

  <article class="intro">
    <h2>Miteinander leben, herzlich umsorgen</h2>
    <p><em>Pflege Lindner</em> - Wir sind Ihr zuverlässiger ambulanter Pflegedienst für Mülheim an der Ruhr, Süd-Duisburg, Süd- &amp; West-Essen, Süd-Oberhausen, Ratingen &amp; Lintorf.</p>
    <p>Mit dem Grundsatz <em>„Miteinander leben, herzlich umsorgen“</em> verpflichten wir uns, jedem Patienten nicht nur professionelle Pflege, sondern auch ein Gefühl von familiärer Geborgenheit und Respekt zu bieten. In dieser Atmosphäre des Vertrauens möchten wir unseren Patienten und ihren Familien Sicherheit und eine stetige Verbesserung der Lebensqualität bieten.</p>
  </article>

  <footer class="footer">
    <ul class="contact contact--address">
      <li><span class="spacer"></span><strong>Pflege Lindner</strong></li>
      <li><svg class="icon" viewBox="0 0 14 14"><path d="M1.5 7 7 2l5.5 5M3 6v6h8V6"/></svg>Auenweg 7</li>
      <li><span class="spacer"></span>45999 Lindenfeld</li>
    </ul>
    <ul class="contact contact--web">
      <li><svg class="icon" viewBox="0 0 14 14"><path d="M3 1.5 5 4 4 5.5c.8 1.8 2.2 3.2 4 4L9.5 8.5 12 10.5 10.5 12.5C6 12 2 8 1.5 3.5Z"/></svg>0208 - 55012300</li>
      <li><svg class="icon" viewBox="0 0 14 14"><circle cx="7" cy="7" r="5.5"/><ellipse cx="7" cy="7" rx="2.4" ry="5.5"/><path d="M1.5 7h11"/></svg>www.pflege-lindner.de</li>
      <li><svg class="icon" viewBox="0 0 14 14"><rect x="1.5" y="3" width="11" height="8"/><path d="m1.5 3 5.5 4.5L12.5 3"/></svg>info@pflege-lindner.de</li>
    </ul>
  </footer>
</section>

<section class="page page--back">
  <div class="photo" role="img" aria-label="Foto: Pflegerin und Seniorin sitzen auf einem Sofa und schauen gemeinsam ein Fotoalbum an"></div>
  <div class="brand">
    <span class="brand-mark"></span>
    <div>
      <div class="brand-name">Pflege Lindner</div>
      <div class="brand-tag">Miteinander leben, herzlich umsorgen</div>
    </div>
  </div>
  <div class="band-dark"></div>
  <div class="band-accent"></div>

  <article class="services">
    <h2>Das können wir für Sie tun:</h2>
    <h3>Behandlungspflege</h3>
    <ul>
      <li>Professionelle Wundversorgung und Verbandswechsel</li>
      <li>Zuverlässige Medikamentengabe und Injektionen</li>
      <li>Auf individuelle Bedürfnisse abgestimmte Pflege</li>
    </ul>
    <h3>Grundpflege</h3>
    <ul>
      <li>Assistenz bei Routinen (Baden, Ankleiden und Körperpflege)</li>
      <li>Unterstützung bei Mobilität und Erhalt der Selbstständigkeit</li>
      <li>Hilfe bei Nahrungs- und Flüssigkeitsaufnahme</li>
    </ul>
    <h3>Betreuung &amp; Hauswirtschaft</h3>
    <ul>
      <li>Unterstützung bei hauswirtschaftlichen Aufgaben</li>
      <li>Hilfe bei Einkäufen oder Behördengängen</li>
      <li>Gemeinsame Aktivitäten und sozialer Austausch</li>
    </ul>
  </article>

  <footer class="footer">
    <div class="footer-col footer-col--steps">
      <h4>So schnell kommt unser Pflegedienst:</h4>
      <ul>
        <li>Rufen Sie uns an: 0208 - 550 123 00</li>
        <li>Wir kommen bei Ihnen vorbei</li>
        <li>Sie erhalten ein Angebot</li>
        <li>Die Pflege beginnt am nächsten Tag</li>
      </ul>
    </div>
    <div class="divider"></div>
    <div class="footer-col footer-col--care">
      <h4>Sie liegen uns am Herzen.</h4>
      <p>Daher werden Patienten bei uns ohne lange Wartezeiten aufgenommen.</p>
    </div>
  </footer>
</section>

</body>
</html>
```